Our Clean Energy Investment Model

Brightmora is a clean energy investment firm that finances community-based solar projects. We are looking for a graphic that displays our investment model and conveys the process of how we put capital to work to generate short- and long-term impact. In the attached document, please find the copy we would like to see in each section. The graphic should be able to easily fit in a PowerPoint slide – ½ of the slide under a header.

Each section, beginning with inputs, should build on one another to reach the “Shape a Greener Power Tomorrow” section in an easy-to-follow flow. The final section, displaying WCA GPT’s, should use the WCA icons, but serve as an addendum and not as part of the flow. Lastly, the graphic should use our company colors of orange (#F29d42), blue (#0c5c7c), and/or white.

Target Market(s)

Clean energy investors

Industry/Entity Type

renewable energy

Colors
0054AA
0677BA
7BADD7
CADEEF
E8F1F8
F0912C
F2A743
F7CA91
FBE8D2
FDF5EE

Requirements
Must have
• Able to fit in a PowerPoint slide; usage of company colors of orange (#F29d42), blue (#0c5c7c), and/or white.

```html
<!DOCTYPE html>
<html lang="en">
<head>
<meta charset="utf-8">
<title>Brightmora Clean Energy Investment Model</title>
<link rel="stylesheet" href="https://fonts.googleapis.com/css2?family=Figtree:wght@400;700&display=swap">
<style>
  :root {
    --blue-deep: #0c5c7c;
    --blue-bright: #0677BA;
    --blue-halo: #CADEEF;
    --blue-pill: #D6E6F3;
    --orange: #F2A743;
    --orange-halo: #FBE8D2;
    --white: #ffffff;
  }
  html, body {
    margin: 0;
    padding: 0;
    width: 1200px;
    height: 394px;
    overflow: hidden;
    background: var(--white);
  }
  .model {
    display: block;
    width: 1200px;
    height: 394px;
    font-family: "Figtree", sans-serif;
  }
  .connector { fill: none; stroke: var(--blue-deep); stroke-width: 1.3; }
  .bullet { fill: var(--blue-deep); }
  .pill { fill: var(--blue-pill); }
  .pill-label { fill: var(--blue-deep); font-size: 7px; font-weight: 400; }
  .stage-halo { fill: var(--blue-halo); }
  .stage { fill: var(--blue-deep); }
  .stage-label { fill: var(--white); font-size: 11.5px; font-weight: 700; text-anchor: middle; }
  .flow-arrow { fill: var(--blue-deep); }
  .horizon { fill: var(--blue-bright); }
  .horizon-label { fill: var(--white); font-size: 11.5px; font-weight: 400; text-anchor: middle; }
  .goal-halo { fill: var(--orange-halo); }
  .goal { fill: var(--orange); }
  .goal-label { fill: var(--white); font-size: 10.5px; font-weight: 700; text-anchor: middle; }
  .partner-mark { fill: var(--blue-bright); }
  .partner-name { fill: var(--blue-bright); font-size: 18px; font-weight: 700; }
</style>
</head>
<body>
<svg class="model" viewBox="0 0 1200 394" xmlns="http://www.w3.org/2000/svg" role="img" aria-label="Brightmora investment model: Partner with Communities, Build for Impact, Shape a Greener Power Tomorrow, leading to WCA Green Power Targets">

  <g class="group-inputs">
    <path class="connector" d="M87 80 V165 Q87 169 91 169 H157 Q161 169 161 173 V187"/>
    <g>
      <circle class="bullet" cx="87" cy="80" r="2.2"/><line class="connector" x1="91" y1="80" x2="96" y2="80"/>
      <rect class="pill" x="98" y="74" width="173" height="12" rx="6"/>
      <text class="pill-label" x="100" y="82.5">Diverse Community Partners and Property Types</text>
    </g>
    <g>
      <circle class="bullet" cx="87" cy="103" r="2.2"/><line class="connector" x1="91" y1="103" x2="96" y2="103"/>
      <rect class="pill" x="98" y="97" width="77" height="12" rx="6"/>
      <text class="pill-label" x="100" y="105.5">Committed Investors</text>
    </g>
    <g>
      <circle class="bullet" cx="87" cy="126" r="2.2"/><line class="connector" x1="91" y1="126" x2="96" y2="126"/>
      <rect class="pill" x="98" y="120" width="135" height="12" rx="6"/>
      <text class="pill-label" x="100" y="128.5">Skilled, Local Developers and Installers</text>
    </g>
    <g>
      <circle class="bullet" cx="87" cy="149" r="2.2"/><line class="connector" x1="91" y1="149" x2="96" y2="149"/>
      <rect class="pill" x="98" y="143" width="42" height="12" rx="6"/>
      <text class="pill-label" x="100" y="151.5">Brightmora</text>
    </g>
    <ellipse class="stage-halo" cx="163" cy="228" rx="46" ry="37"/>
    <ellipse class="stage" cx="163" cy="228" rx="41" ry="33"/>
    <text class="stage-label" x="163" y="226">Partner with</text>
    <text class="stage-label" x="163" y="238.5">Communities</text>
  </g>

  <path class="flow-arrow" d="M221 228.4 L327 226 L327 222 L338 228 L327 234 L327 230 Z"/>

  <g class="group-build">
    <path class="connector" d="M337 81 V165 Q337 169 341 169 H397 Q401 169 401 173 V187"/>
    <g>
      <circle class="bullet" cx="337" cy="81" r="2.2"/><line class="connector" x1="341" y1="81" x2="347" y2="81"/>
      <rect class="pill" x="349" y="75" width="98" height="12" rx="6"/>
      <text class="pill-label" x="353" y="83.5">Comprehensive Underwriting</text>
    </g>
    <g>
      <circle class="bullet" cx="337" cy="98" r="2.2"/><line class="connector" x1="341" y1="98" x2="347" y2="98"/>
      <rect class="pill" x="349" y="92" width="62" height="12" rx="6"/>
      <text class="pill-label" x="353" y="100.5">Deal Structuring</text>
    </g>
    <g>
      <circle class="bullet" cx="337" cy="115" r="2.2"/><line class="connector" x1="341" y1="115" x2="347" y2="115"/>
      <rect class="pill" x="349" y="109" width="156" height="12" rx="6"/>
      <text class="pill-label" x="353" y="117.5">Development and Construction Management</text>
    </g>
    <g>
      <circle class="bullet" cx="337" cy="133" r="2.2"/><line class="connector" x1="341" y1="133" x2="347" y2="133"/>
      <rect class="pill" x="349" y="127" width="71" height="12" rx="6"/>
      <text class="pill-label" x="353" y="135.5">Solar Impact Fund</text>
    </g>
    <g>
      <circle class="bullet" cx="337" cy="150" r="2.2"/><line class="connector" x1="341" y1="150" x2="347" y2="150"/>
      <rect class="pill" x="349" y="144" width="71" height="12" rx="6"/>
      <text class="pill-label" x="353" y="152.5">Asset Management</text>
    </g>
    <ellipse class="stage-halo" cx="401" cy="228" rx="46" ry="37"/>
    <ellipse class="stage" cx="401" cy="228" rx="41" ry="33"/>
    <text class="stage-label" x="401" y="226">Build for</text>
    <text class="stage-label" x="401" y="238.5">Impact</text>
  </g>

  <path class="flow-arrow" d="M460 228.4 L566 226 L566 222 L577 228 L566 234 L566 230 Z"/>

  <g class="group-future">
    <path class="connector" d="M588 55 V143 Q588 147 592 147 H604"/>
    <g>
      <circle class="bullet" cx="588" cy="55" r="2.2"/><line class="connector" x1="592" y1="55" x2="598" y2="55"/>
      <rect class="pill" x="601" y="49" width="49" height="12" rx="6"/>
      <text class="pill-label" x="604" y="57.5">Green Jobs</text>
    </g>
    <g>
      <circle class="bullet" cx="588" cy="72" r="2.2"/><line class="connector" x1="592" y1="72" x2="598" y2="72"/>
      <rect class="pill" x="601" y="66" width="64" height="12" rx="6"/>
      <text class="pill-label" x="604" y="74.5">Carbon Reduction</text>
    </g>
    <g>
      <circle class="bullet" cx="588" cy="89" r="2.2"/><line class="connector" x1="592" y1="89" x2="598" y2="89"/>
      <rect class="pill" x="601" y="83" width="56" height="12" rx="6"/>
      <text class="pill-label" x="604" y="91.5">Energy Savings</text>
    </g>
    <g>
      <circle class="bullet" cx="588" cy="106" r="2.2"/><line class="connector" x1="592" y1="106" x2="598" y2="106"/>
      <rect class="pill" x="601" y="100" width="58" height="12" rx="6"/>
      <text class="pill-label" x="604" y="108.5">Investor Returns</text>
    </g>
    <g>
      <circle class="bullet" cx="588" cy="124" r="2.2"/><line class="connector" x1="592" y1="124" x2="598" y2="124"/>
      <rect class="pill" x="601" y="118" width="100" height="12" rx="6"/>
      <text class="pill-label" x="604" y="126.5">Democratized Energy Future</text>
    </g>

    <rect class="horizon" x="601" y="138" width="57" height="18" rx="9"/>
    <text class="horizon-label" x="629.5" y="151">Today</text>

    <path class="flow-arrow" d="M636.2 185 L635.6 170 L631 170 L637 160 L643 170 L638.4 170 L637.8 185 Z"/>

    <ellipse class="stage-halo" cx="637" cy="226" rx="46" ry="37"/>
    <ellipse class="stage" cx="637" cy="226" rx="41" ry="33"/>
    <text class="stage-label" x="637" y="218">Shape a</text>
    <text class="stage-label" x="637" y="230.5">Greener Power</text>
    <text class="stage-label" x="637" y="243">Tomorrow</text>

    <path class="flow-arrow" d="M636.2 268 L635.6 283 L631 283 L637 293 L643 283 L638.4 283 L637.8 268 Z"/>

    <path class="connector" d="M604 309 H592 Q588 309 588 313 V348"/>
    <rect class="horizon" x="600" y="300" width="73" height="18" rx="9"/>
    <text class="horizon-label" x="636.5" y="313">Tomorrow</text>

    <g>
      <circle class="bullet" cx="588" cy="332" r="2.2"/><line class="connector" x1="592" y1="332" x2="598" y2="332"/>
      <rect class="pill" x="601" y="326" width="163" height="12" rx="6"/>
      <text class="pill-label" x="604" y="334.5">Put Climate Change and Inequality on the Ropes</text>
    </g>
    <g>
      <circle class="bullet" cx="588" cy="348" r="2.2"/><line class="connector" x1="592" y1="348" x2="598" y2="348"/>
      <rect class="pill" x="601" y="342" width="99" height="12" rx="6"/>
      <text class="pill-label" x="604" y="350.5">Mainstream Impact Investing</text>
    </g>
  </g>

  <path class="flow-arrow" d="M691 228.4 L797 226 L797 222 L808 228 L797 234 L797 230 Z"/>

  <g class="group-goals">
    <ellipse class="goal-halo" cx="888" cy="226" rx="66" ry="37"/>
    <ellipse class="goal" cx="888" cy="226" rx="61" ry="33"/>
    <text class="goal-label" x="888" y="222">WCA Green Power</text>
    <text class="goal-label" x="888" y="234.5">Targets</text>

    <g class="partner">
      <circle class="partner-mark" cx="1000" cy="226" r="8"/>
      <text class="partner-name" x="1014" y="232.5">WCA</text>
    </g>
  </g>
</svg>
</body>
</html>
```